I am a general contractor in Portland, Or. I would like a clean and simple design layout, maybe using the "didot" font, blue and dark bronze in colors are preferred. On one side of the card, it would be nice to have a logo(attached photo) and business name(KBT Construction). I don't need my job title on the card, just some thing along the lines of "harold pike, general contractor". Thanks much.

Target Market(s)

Adults from 30-55 years old. Middle to upper class.

Industry/Entity Type

Contractor

Contact Information for Business Card

KBT Construction
Harold M. Pike
2943 NE 71st Ave.
Portland, Or. 97288
503.627.9184

Font styles to use
Other font styles liked:
• didot

Colors
3277b5
7f7f7f

Requirements
Should not have
• Too much going on.

```html
<!DOCTYPE html>
<html lang="en">
<head>
<meta charset="utf-8">
<title>KBT Construction – Business Card</title>
<link rel="stylesheet" href="https://fonts.googleapis.com/css2?family=Exo+2:wght@400;500;600;700&display=swap">
<style>
  :root {
    --backdrop: #d9d9d7;
    --card-light: #ffffff;
    --card-shade: #d8d8d8;
    --brand-blue: #0aa3e3;
    --ink-dark: #1f1f1f;
    --ink-grey: #3a3a3a;
    --text-light: #ffffff;
  }
  html, body {
    margin: 0;
    padding: 0;
    width: 1200px;
    height: 869px;
    overflow: hidden;
    background: var(--backdrop);
    font-family: "Exo 2", "Helvetica Neue", Arial, sans-serif;
  }
  .canvas {
    position: relative;
    width: 1200px;
    height: 869px;
    display: flex;
    align-items: center;
    justify-content: center;
    gap: 40px;
  }
  .card {
    width: 540px;
    height: 309px;
    box-shadow: 0 6px 18px rgba(0,0,0,0.18);
    display: block;
  }
  .brand-name { font-weight: 700; fill: var(--brand-blue); }
  .brand-dot { fill: var(--ink-dark); }
  .address-line { font-weight: 500; fill: var(--text-light); font-size: 15px; }
  .person-name { font-weight: 500; fill: var(--ink-grey); font-size: 24px; letter-spacing: 1.5px; }
  .person-title { font-weight: 500; fill: var(--ink-grey); font-size: 10.5px; letter-spacing: 1.2px; }
  .contact-text { font-weight: 400; fill: var(--text-light); font-size: 13.5px; letter-spacing: 0.5px; }
  .icon-tile { fill: var(--text-light); }
  .icon-glyph { fill: none; stroke: var(--ink-dark); stroke-width: 1.4; }
  .icon-solid { fill: var(--ink-dark); }
  .band-blue { fill: var(--brand-blue); }
  .band-dark { fill: var(--ink-dark); }
</style>
</head>
<body>
<main class="canvas">

  <!-- Logo side -->
  <svg class="card card-front" viewBox="0 0 540 309" role="img" aria-label="KBT Construction logo side">
    <defs>
      <linearGradient id="front-paper" x1="0" y1="0" x2="1" y2="1">
        <stop offset="0" stop-color="#f1f1f1"/>
        <stop offset="0.5" stop-color="#ffffff"/>
        <stop offset="1" stop-color="#d6d6d6"/>
      </linearGradient>
    </defs>
    <rect width="540" height="309" fill="url(#front-paper)"/>
    <g class="brand-lockup">
      <circle class="brand-dot" cx="158" cy="154" r="26"/>
      <text class="brand-name" x="196" y="163" font-size="27">KBT Construction</text>
    </g>
  </svg>

  <!-- Contact side -->
  <svg class="card card-back" viewBox="0 0 540 309" role="img" aria-label="KBT Construction contact side">
    <defs>
      <linearGradient id="back-paper" x1="0" y1="0" x2="1" y2="0.6">
        <stop offset="0" stop-color="#ececec"/>
        <stop offset="0.55" stop-color="#ffffff"/>
        <stop offset="1" stop-color="#d0d0d0"/>
      </linearGradient>
    </defs>
    <rect width="540" height="309" fill="url(#back-paper)"/>

    <!-- logo lockup -->
    <g class="brand-lockup">
      <circle class="brand-dot" cx="42" cy="58" r="17"/>
      <text class="brand-name" x="66" y="65" font-size="20">KBT Construction</text>
    </g>

    <!-- dark body and blue bands -->
    <polygon class="band-dark" points="0,118 400,118 420,150 540,150 540,309 0,309"/>
    <polygon class="band-blue" points="0,96 400,96 420,128 425,150 410,150 400,126 0,126"/>
    <polygon class="band-blue" points="0,262 540,262 540,282 0,282"/>

    <text class="address-line" x="38" y="117">2943 NE 71st Ave. Portland, Or. 97288</text>

    <!-- name block -->
    <text class="person-name" x="512" y="116" text-anchor="end">HAROLD PIKE</text>
    <text class="person-title" x="512" y="134" text-anchor="end">GENERAL CONTRACTOR</text>

    <!-- web -->
    <rect class="icon-tile" x="20" y="150" width="20" height="20" rx="3"/>
    <circle class="icon-glyph" cx="30" cy="160" r="6"/>
    <ellipse class="icon-glyph" cx="30" cy="160" rx="2.6" ry="6"/>
    <line class="icon-glyph" x1="24" y1="160" x2="36" y2="160"/>
    <text class="contact-text" x="50" y="165">www.kbtbuildco.com</text>

    <!-- email -->
    <rect class="icon-tile" x="20" y="180" width="20" height="20" rx="3"/>
    <rect class="icon-glyph" x="24" y="185" width="12" height="9"/>
    <polyline class="icon-glyph" points="24,185 30,190 36,185"/>
    <text class="contact-text" x="50" y="195">harold@kbtbuildco.com</text>

    <!-- phone -->
    <rect class="icon-tile" x="340" y="190" width="20" height="20" rx="3"/>
    <path class="icon-solid" d="M345 194 l3 0 l1.5 4 l-2 1.2 a8 8 0 0 0 4.3 4.3 l1.2 -2 l4 1.5 l0 3 a2 2 0 0 1 -2 2 a13 13 0 0 1 -12 -12 a2 2 0 0 1 2 -2z"/>
    <text class="contact-text" x="370" y="205">503 627 9184</text>

    <!-- mobile -->
    <rect class="icon-tile" x="340" y="220" width="20" height="20" rx="3"/>
    <rect class="icon-glyph" x="345.5" y="223.5" width="9" height="13" rx="1.5"/>
    <line class="icon-glyph" x1="348" y1="233.5" x2="352" y2="233.5"/>
    <text class="contact-text" x="370" y="235">503 627 9184</text>
  </svg>

</main>
</body>
</html>
```